Bright Path Attorneys Billboard Design for Personal Injury Law Firm

Need a billboard design that we can use for different versions. 1400px X 400px jpeg or png
I have attached the logo and the attorney for the billboard. Attorney Marla Benning
Here is a link to our current website brightpathlegalgroup.example

HEADLINE: HIT BY A TRUCK?
SUBHEAD: NO FEE. BIG FIGHT.
877-GRANTLY

HEADLINE: ACCIDENT?
SUBHEAD: NO FEE, UNLESS WE WIN!
877-GRANTLY

HEADLINE: BIG TRUCK. BIG CASE.
SUBHEAD: YOU PAY $0 UPFRONT
877-GRANTLY

Target Market(s)

People in Car Accident

Industry/Entity Type

Personal Injury Attorneys

```html
<!DOCTYPE html>
<html lang="en">
<head>
<meta charset="UTF-8">
<title>Bright Path Attorneys – Billboard</title>
<link href="https://fonts.googleapis.com/css2?family=Anton&family=Montserrat:wght@700;800&display=swap" rel="stylesheet">
<style>
  :root {
    --stage: #b3b3b3;
    --board-dark: #1b1e23;
    --accent-green: #5ad23a;
    --band-green: #5fd63d;
    --ink-dark: #1b1e23;
    --white: #ffffff;
    --photo-deep: #23282b;
    --photo-mid: #4a5156;
    --photo-light: #7d858a;
  }
  * { margin: 0; padding: 0; box-sizing: border-box; }
  html, body {
    width: 1200px;
    height: 414px;
    overflow: hidden;
    background: var(--stage);
  }
  .billboard {
    position: absolute;
    left: 80px;
    top: 58px;
    width: 1040px;
    height: 296px;
    background: var(--board-dark);
    overflow: hidden;
    box-shadow: 0 4px 10px rgba(0, 0, 0, 0.35);
  }
  .headline {
    position: absolute;
    left: 36px;
    top: 22px;
    font-family: "Anton", "Oswald", sans-serif;
    font-weight: 400;
    font-size: 104px;
    line-height: 1;
    letter-spacing: 3px;
    color: var(--accent-green);
    white-space: nowrap;
  }
  .subhead {
    position: absolute;
    left: 37px;
    top: 118px;
    font-family: "Montserrat", sans-serif;
    font-weight: 800;
    font-size: 70px;
    line-height: 1;
    letter-spacing: -0.5px;
    color: var(--white);
    white-space: nowrap;
  }
  .phone-band {
    position: absolute;
    left: 0;
    top: 204px;
    width: 860px;
    height: 92px;
    background: var(--band-green);
  }
  .phone-number {
    position: absolute;
    left: 40px;
    top: 0;
    font-family: "Montserrat", sans-serif;
    font-weight: 800;
    font-size: 96px;
    line-height: 1;
    letter-spacing: -1px;
    color: var(--ink-dark);
    white-space: nowrap;
  }
  .vehicle-photo {
    position: absolute;
    z-index: 1;
    left: 780px;
    top: 70px;
    width: 260px;
    height: 226px;
    background: radial-gradient(ellipse at 55% 45%, var(--photo-light) 0%, var(--photo-mid) 45%, var(--photo-deep) 100%);
  }
  .firm-mark {
    position: absolute;
    z-index: 2;
    left: 740px;
    top: 26px;
    display: flex;
    align-items: center;
    gap: 12px;
  }
  .firm-mark__dot {
    width: 36px;
    height: 36px;
    border-radius: 50%;
    background: var(--accent-green);
  }
  .firm-mark__name {
    font-family: "Montserrat", sans-serif;
    font-weight: 700;
    font-size: 19px;
    line-height: 1.15;
    color: var(--white);
    white-space: nowrap;
  }
</style>
</head>
<body>
  <main class="billboard">
    <h1 class="headline">HIT BY A TRUCK?</h1>
    <p class="subhead">NO FEE. BIG FIGHT.</p>
    <div class="phone-band">
      <p class="phone-number">877-GRANTLY</p>
    </div>
    <div class="vehicle-photo" role="img" aria-label="Photo of a dark car with a crushed front end after a truck collision"></div>
    <div class="firm-mark">
      <span class="firm-mark__dot"></span>
      <p class="firm-mark__name">Bright Path<br>Attorneys</p>
    </div>
  </main>
</body>
</html>
```